Website created on Plorvix.com

I have a telecommunications company and i would like my website built on plorvix.com as this platform is easy for me to change in the future so the site needs to be made so i can change it when i need to. Also I have found Plorvix is very good for SEO setup
Examples of websites i like as they are clean and corporate www.dastrelo.com.au (on this site there are menus on the right hand side which changes the content on the same page I would like the also www.kovantirel.com.au
My company sells business phone systems we sell the following products
1. Hosted PBX (This is the main product/service we sell)
2. Tusrok products (Tusrok has a range of products Phone systems, Gateways and Software we sell all products)
3. Brondavi Phones (we sell the following Brondavi phones T46G, T42G, T41G, T28P, T26P, T22P, T20P, VP530, W52P, EXP39, EXP40
4. ZelPBX (www.quimbrel.com) we sell SoHo and all the U series plus the add on's
5. VoIP plans (this is a outbound phone service for business customer)
1. business starter ($0 month 0 call included .12c local calls .24c mobile calls
2. business saver ($25 month 250 local calls included .10c local calls .22c mobile calls
3. business super ($50 month 500 local calls included .09c local calls .20c mobile calls
4. business extreme ($100 month 1000 local calls included .08c local calls .18c mobile calls
home page
custom corporate banners for each product/service 1. Hosted PBX 2. VoIP Plans 3. Brondavi Phones 4. ZelPBX 5. Tusrok, Which will rotate every 4 seconds
next will be displaying the VoIP plans with links to the plans pages
next icons of 1. Hosted PBX, 2. Brondavi phones 3. ZelPBX 4. Tusrok with links to the right page within the site
next a section with a description and design of what the business can do you the customer, please give me some examples
Product pages for all products/services Hosted PBX, Brondavi, ZelPbx, Tusrok and VoIP plans
Please make a pages for Headsets and I will attached the brands later
The aim is to have a clean white corporate website that ranks very will in fenwora that I can manage in the future
Please do not copy my existing site
small to medium business
Telecommunications

```html
<!DOCTYPE html>
<html lang="en">
<head>
<meta charset="utf-8">
<title>Callvessa — Hosted PBX for Business</title>
<link rel="stylesheet" href="https://fonts.googleapis.com/css2?family=Open+Sans:wght@300;400;600&family=Source+Sans+3:wght@400;600&family=Arimo:wght@400;700&display=swap">
<style>
  :root {
    --brand-blue: #0b5a9c;
    --accent-blue: #1a73e8;
    --button-blue: #1471e6;
    --button-edge: #0d5fc9;
    --ink: #222;
    --body-grey: #666;
    --card-ink: #444;
    --footer-head: #555;
    --footer-link: #9a9a9a;
    --rule: #e2e2e2;
    --panel-edge: #dcdcdc;
  }
  * { margin: 0; padding: 0; box-sizing: border-box; }
  html, body { width: 1200px; height: 1054px; overflow: hidden; background: #fff; }
  body { position: relative; font-family: "Open Sans", sans-serif; color: var(--ink); }

  .top-bar { position: absolute; top: 0; left: 0; width: 1200px; height: 5px; background: var(--brand-blue); }

  .site-header { position: absolute; top: 5px; left: 66px; width: 1066px; height: 103px; border-bottom: 1px solid var(--rule); }
  .brand { position: absolute; left: 0; top: 36px; display: flex; align-items: center; gap: 10px; }
  .brand-mark { width: 14px; height: 14px; background: var(--brand-blue); }
  .brand-name { font-family: "Open Sans", sans-serif; font-weight: 600; font-size: 34px; color: var(--brand-blue); letter-spacing: -0.5px; }
  .call-line { position: absolute; right: 0; top: 27px; font-size: 14px; color: #555; letter-spacing: 0.3px; }
  .main-nav { position: absolute; right: 0; top: 72px; display: flex; gap: 22px; }
  .main-nav a { position: relative; font-size: 14px; color: var(--ink); text-decoration: none; padding: 0 8px 12px; }
  .main-nav a.is-active::after { content: ""; position: absolute; left: 0; right: 0; bottom: 0; height: 4px; background: var(--accent-blue); }

  .hero { position: absolute; left: 65px; top: 143px; width: 1066px; height: 352px; border: 1px solid var(--panel-edge); border-radius: 8px;
          background: linear-gradient(#f4f4f4 0%, #fff 30%, #fff 80%, #f1f1f1 100%); box-shadow: 0 2px 4px rgba(0,0,0,.12); }
  .hero-copy { position: absolute; left: 76px; top: 78px; width: 455px; }
  .hero-title { font-weight: 300; font-size: 26px; color: #222; margin-bottom: 12px; }
  .hero-text { font-size: 14.5px; line-height: 1.4; color: var(--body-grey); }
  .btn-primary { position: absolute; left: 76px; top: 207px; width: 141px; height: 55px; background: var(--button-blue); color: #fff; border: 1px solid var(--button-edge);
                 border-radius: 2px; font-size: 15px; display: flex; align-items: center; justify-content: center; text-decoration: none; }
  .hero-photo { position: absolute; left: 545px; top: 42px; width: 420px; height: 250px;
                background: radial-gradient(closest-side, #4a4a4a 0%, #8a8a8a 50%, rgba(255,255,255,0) 100%); }

  .features { position: absolute; left: 67px; top: 536px; width: 1064px; display: flex; justify-content: space-between; }
  .feature { width: 245px; }
  .feature-photo { height: 110px; border: 1px solid var(--panel-edge); border-radius: 8px; box-shadow: 0 2px 3px rgba(0,0,0,.1);
                   background: radial-gradient(ellipse at 50% 50%, #555 0%, #999 30%, #f2f2f2 55%, #fafafa 100%); }
  .feature-title { font-family: "Source Sans 3", sans-serif; font-weight: 400; font-size: 20px; color: var(--brand-blue); margin: 22px 0 6px 4px; }
  .feature-text { font-family: "Source Sans 3", sans-serif; font-size: 15px; line-height: 18.5px; color: var(--card-ink); text-align: justify; padding: 0 12px 0 4px; }

  .site-footer { position: absolute; left: 0; top: 874px; width: 1200px; height: 180px; border-top: 1px solid var(--rule);
                 background: linear-gradient(#fff 0%, #fff 70%, #ececec 100%); font-family: "Arimo", sans-serif; }
  .footer-rule { position: absolute; left: 67px; top: 0; width: 1px; height: 141px; background: var(--rule); }
  .footer-col { position: absolute; top: 20px; }
  .footer-col h3 { font-size: 13.5px; font-weight: 700; color: var(--footer-head); margin-bottom: 2px; }
  .footer-col a { display: block; font-size: 12px; line-height: 17.7px; color: var(--footer-link); text-decoration: none; }
  .col-products { left: 93px; } .col-addons { left: 282px; } .col-general { left: 503px; } .col-legal { left: 659px; }
  .footer-brand { position: absolute; left: 905px; top: 52px; display: flex; align-items: center; gap: 9px; }
  .footer-brand .brand-name { font-size: 32px; }
  .bottom-bar { position: absolute; left: 0; bottom: 0; width: 1200px; height: 7px; background: var(--brand-blue); }
</style>
</head>
<body>
  <div class="top-bar"></div>

  <header class="site-header">
    <div class="brand"><span class="brand-mark"></span><span class="brand-name">Callvessa</span></div>
    <div class="call-line">CALL 908 2716 354</div>
    <nav class="main-nav">
      <a href="#" class="is-active">HOME</a>
      <a href="#">PRODUCT</a>
      <a href="#">SUPPORT</a>
      <a href="#">PARTNER</a>
      <a href="#">CONTACT</a>
    </nav>
  </header>

  <section class="hero">
    <div class="hero-copy">
      <h1 class="hero-title">Hosted PBX for Business</h1>
      <p class="hero-text">Lorem ipsum dolor sit amet, consectetur adipiscing elit. Phasellus dignissim accumsan pulvinar. Mauris tempus diam sit amet auctor luctus.</p>
    </div>
    <a href="#" class="btn-primary">Learn More</a>
    <div class="hero-photo" role="img" aria-label="Photo of a business desk phone with handset and display"></div>
  </section>

  <section class="features">
    <article class="feature">
      <div class="feature-photo" role="img" aria-label="Photo of a business desk phone"></div>
      <h2 class="feature-title">Hosted PBX for Business</h2>
      <p class="feature-text">Lorem ipsum dolor sit amet, con&shy;sectetur adipiscing elit. Sed ullam&shy;corper, tellus quis vulputate fermentum, risus turpis feugiat leo, condimentum faucibus dui metus.</p>
    </article>
    <article class="feature">
      <div class="feature-photo" role="img" aria-label="Photo of a business desk phone"></div>
      <h2 class="feature-title">Hosted PBX for Business</h2>
      <p class="feature-text">Lorem ipsum dolor sit amet, con&shy;sectetur adipiscing elit. Sed ullam&shy;corper, tellus quis vulputate fermentum, risus turpis feugiat leo, condimentum faucibus dui metus .</p>
    </article>
    <article class="feature">
      <div class="feature-photo" role="img" aria-label="Photo of a business desk phone"></div>
      <h2 class="feature-title">Hosted PBX for Business</h2>
      <p class="feature-text">Lorem ipsum dolor sit amet, con&shy;sectetur adipiscing elit. Sed ullam&shy;corper, tellus quis vulputate fermentum, risus turpis feugiat leo, condimentum faucibus dui metus .</p>
    </article>
    <article class="feature">
      <div class="feature-photo" role="img" aria-label="Photo of a business desk phone"></div>
      <h2 class="feature-title">Hosted PBX for Business</h2>
      <p class="feature-text">Lorem ipsum dolor sit amet, con&shy;sectetur adipiscing elit. Sed ullam&shy;corper, tellus quis vulputate fermentum, risus turpis feugiat leo, condimentum faucibus dui metus s</p>
    </article>
  </section>

  <footer class="site-footer">
    <div class="footer-rule"></div>
    <div class="footer-col col-products">
      <h3>Products</h3>
      <a href="#">Business VoIP Plans</a><a href="#">Hosted PBX</a><a href="#">Managed PBX</a><a href="#">Fax to Email</a><a href="#">Hardware</a>
    </div>
    <div class="footer-col col-addons">
      <h3>Add-on Services</h3>
      <a href="#">1300 &amp; 1800 Numbers</a><a href="#">Teleconferencing</a><a href="#">Number Portability</a><a href="#">Private IP</a><a href="#">Interactive Voice Response</a>
    </div>
    <div class="footer-col col-general">
      <h3>General</h3>
      <a href="#">About us</a><a href="#">Blog</a><a href="#">Partners</a><a href="#">Contact us</a><a href="#">Support</a>
    </div>
    <div class="footer-col col-legal">
      <h3>Legal &amp; Regulatory</h3>
      <a href="#">Fair Use Policy</a><a href="#">Privacy Policy</a><a href="#">Terms &amp; Conditions</a>
    </div>
    <div class="footer-brand"><span class="brand-mark"></span><span class="brand-name">Callvessa</span></div>
    <div class="bottom-bar"></div>
  </footer>
</body>
</html>
```